Fernlymentor: an app for coaches and students in golf and fitness

I currently have an app that is called Fernlymentor and I am redoing the app completely and with this I am looking for a cool design for the app. I am not happy with the design as it is at the moment. The app should have a nice welcome and when you are logged in the dashboard must be very modern. It is a golf app that have 2 type of users. 1 user is the coach and the other user is the student. Those users can see different things of course.
The coach is normally paying a subscription charge for using the app but I want to get the students to pay for different tools that I will be offering via the app. To me the dashboard and the homepage of the app (once you have downloaded the app) is important. Here I would like to get the student as well as the coach the feeling of what the app can offer. The app offers features like Calendar (here the student can book the coach via the calendar), Chat (here the coach and the student can chat with each other as well as the coach can creat group chats with several students), Notes (here the coach as well as the student can create notes for their lessons), video tips (here the coach can upload video tips for his/her students, online lesson (the student can take online lessons by uploading recorded videos..and so on

Target Market(s)

Sport coaches (for start it will be mostly golf coaches)

Industry/Entity Type

Sports

Font styles to use
Sans Serif

Colors
0054AA
0677BA
7BADD7
CADEEF
E8F1F8

Requirements
Must have
• modern design and easy navigation.
Nice to have
• It all starts with the dashboard
Should not have
• boring standard style.

```html
<!DOCTYPE html>
<html lang="en">
<head>
<meta charset="utf-8">
<title>Fernlymentor – Golf Coaching App Screens</title>
<link rel="stylesheet" href="https://fonts.googleapis.com/css2?family=Poppins:wght@400;500;600;700&display=swap">
<style>
  :root {
    --bg: #cadeef;
    --navy: #0054aa;
    --blue: #0677ba;
    --sky: #7badd7;
    --mist: #cadeef;
    --ice: #e8f1f8;
    --coral: #f2645a;
    --ink: #1f2f47;
    --muted: #7d8ca3;
    --white: #ffffff;
  }
  * { box-sizing: border-box; margin: 0; padding: 0; }
  html, body { width: 1200px; height: 787px; overflow: hidden; }
  body { background: var(--bg); font-family: "Poppins", sans-serif; color: var(--ink); position: relative; }

  .screen { position: absolute; top: 80px; width: 304px; height: 625px; border-radius: 30px; overflow: hidden; background: var(--white); box-shadow: 0 18px 40px rgba(0,84,170,.16); }
  .screen--welcome { left: 92px; background: linear-gradient(160deg, var(--blue), var(--navy)); }
  .screen--dashboard { left: 448px; }
  .screen--progress { left: 808px; }

  .topbar { position: absolute; top: 20px; left: 18px; right: 18px; display: flex; justify-content: space-between; }
  .abs { position: absolute; }
  .center { left: 0; right: 0; text-align: center; }

  .pill { position: absolute; height: 26px; border-radius: 13px; font-size: 12px; font-weight: 500; display: flex; align-items: center; justify-content: center; }

  /* Welcome */
  .brand { top: 262px; font-size: 30px; font-weight: 700; color: var(--white); }
  .pill--signup { top: 462px; left: 102px; width: 100px; background: var(--coral); color: var(--white); }
  .pill--login { top: 506px; left: 102px; width: 100px; background: var(--white); color: var(--navy); }
  .forgot { top: 544px; font-size: 9px; color: var(--white); }

  /* Dashboard */
  .greet { top: 66px; left: 30px; font-size: 13px; line-height: 1.4; }
  .greet strong { display: block; color: var(--navy); font-weight: 600; font-size: 14px; }
  .week { top: 124px; left: 26px; right: 14px; display: flex; justify-content: space-between; }
  .day { width: 30px; text-align: center; font-size: 9px; color: var(--muted); padding: 3px 0; border-radius: 6px; }
  .day b { display: block; font-size: 16px; font-weight: 500; color: var(--ink); }
  .day--active { background: var(--navy); color: var(--white); }
  .day--active b { color: var(--white); }
  .golfer-art { top: 196px; left: 28px; width: 130px; height: 162px; border-radius: 60px 60px 20px 60px; background: linear-gradient(160deg, var(--ice), var(--mist)); }
  .lesson-title { top: 204px; left: 168px; font-size: 14px; font-weight: 600; line-height: 1.3; }
  .lesson-time { top: 252px; left: 168px; font-size: 26px; font-weight: 600; color: var(--navy); }
  .pill--book { top: 306px; left: 168px; width: 104px; background: var(--coral); color: var(--white); }
  .stats { top: 372px; left: 38px; width: 248px; height: 140px; border-radius: 12px; background: linear-gradient(135deg, var(--blue), var(--navy)); color: var(--white); overflow: hidden; }
  .stat { position: absolute; left: 14px; display: flex; align-items: baseline; gap: 8px; font-size: 22px; font-weight: 500; }
  .stat svg { width: 13px; height: 13px; align-self: center; }
  .stat small { font-size: 9px; font-weight: 400; opacity: .85; }
  .stats-label { position: absolute; top: 14px; right: 22px; font-size: 8px; opacity: .85; }
  .navbar { bottom: 36px; left: 26px; right: 26px; display: flex; justify-content: space-between; }

  /* Progress */
  .hero { top: 0; left: 0; right: 0; height: 290px; background: linear-gradient(160deg, var(--blue), var(--navy)); border-radius: 0 0 26px 26px; }
  .title { top: 52px; font-size: 15px; font-weight: 600; color: var(--white); }
  .ring { top: 104px; left: 84px; width: 136px; height: 136px; }
  .ring-label { top: 150px; font-size: 22px; font-weight: 600; color: var(--coral); }
  .ring-sub { top: 182px; font-size: 8px; color: var(--muted); }
  .pill--tools { top: 294px; left: 92px; width: 120px; background: var(--coral); color: var(--white); }
  .tiles { top: 346px; left: 38px; right: 38px; display: flex; justify-content: space-between; }
  .tile { width: 58px; text-align: center; font-size: 9px; color: var(--muted); }
  .tile span { display: flex; align-items: center; justify-content: center; height: 58px; border-radius: 10px; background: var(--ice); margin-bottom: 8px; }
  .tile--active { color: var(--ink); font-weight: 600; }
  .tile--active span { background: var(--coral); }
  .chart { top: 446px; left: 26px; width: 252px; height: 78px; border-radius: 12px; background: linear-gradient(135deg, var(--blue), var(--navy)); padding: 10px 14px 0; }
  .bars { display: flex; justify-content: space-between; align-items: flex-end; height: 44px; }
  .bar { width: 26px; background: var(--white); border-radius: 3px 3px 0 0; }
  .bar--hot { background: var(--coral); }
  .days { display: flex; justify-content: space-between; font-size: 8px; color: var(--white); margin-top: 4px; }
  .days span { width: 26px; text-align: center; }
  .fab { bottom: 38px; left: 138px; width: 28px; height: 28px; border-radius: 50%; background: var(--coral); color: var(--white); font-size: 20px; display: flex; align-items: center; justify-content: center; }
</style>
</head>
<body>

<section class="screen screen--welcome" aria-label="Welcome screen">
  <div class="topbar">
    <svg width="12" height="12" viewBox="0 0 12 12"><path d="M8 2 4 6l4 4" stroke="#fff" stroke-width="2" fill="none"/></svg>
    <svg width="14" height="12" viewBox="0 0 14 12"><path d="M1 2h12M1 6h12M1 10h12" stroke="#fff" stroke-width="2"/></svg>
  </div>
  <h1 class="abs center brand">Fernlymentor</h1>
  <a class="pill pill--signup">Sign Up</a>
  <a class="pill pill--login">Login</a>
  <p class="abs center forgot">Forgot your password?</p>
</section>

<section class="screen screen--dashboard" aria-label="Student dashboard">
  <div class="topbar">
    <svg width="12" height="12" viewBox="0 0 12 12"><path d="M8 2 4 6l4 4" stroke="#1f2f47" stroke-width="2" fill="none"/></svg>
    <svg width="14" height="12" viewBox="0 0 14 12"><path d="M1 2h12M1 6h12M1 10h12" stroke="#1f2f47" stroke-width="2"/></svg>
  </div>
  <p class="abs greet">Hello<strong>Amara</strong></p>
  <div class="abs week" aria-label="Lesson booking calendar">
    <div class="day">Mon<b>8</b></div>
    <div class="day">Tue<b>9</b></div>
    <div class="day">Wed<b>10</b></div>
    <div class="day">Thu<b>11</b></div>
    <div class="day day--active">Fri<b>12</b></div>
    <div class="day">Sat<b>13</b></div>
    <div class="day">Sun<b>14</b></div>
  </div>
  <div class="abs golfer-art" role="img" aria-label="Illustration of a golfer finishing a swing"></div>
  <p class="abs lesson-title">Next lesson with<br>your coach</p>
  <p class="abs lesson-time">10:30 am</p>
  <a class="pill pill--book">Book</a>
  <div class="abs stats">
    <div class="stat" style="top:14px"><svg viewBox="0 0 12 12"><rect x="1" y="2" width="10" height="9" rx="1.5" stroke="#fff" stroke-width="1.6" fill="none"/><path d="M1 5h10M4 0v3M8 0v3" stroke="#fff" stroke-width="1.6"/></svg>3<small>lessons</small></div>
    <div class="stat" style="top:54px"><svg viewBox="0 0 12 12"><path d="M1 2h10v7H5l-3 2V9H1z" fill="#fff"/></svg>12<small>chats</small></div>
    <div class="stat" style="top:94px"><svg viewBox="0 0 12 12"><rect x="0" y="2" width="8" height="8" rx="1.5" fill="#fff"/><path d="M8 5l4-2v6L8 7z" fill="#fff"/></svg>5<small>video tips</small></div>
    <span class="stats-label">This week</span>
    <svg class="abs" style="left:90px;top:30px" width="158" height="110" viewBox="0 0 158 110">
      <path d="M0 110C40 100 50 60 80 50s40-20 60-40" stroke="#fff" stroke-width="2" fill="none"/>
      <circle cx="140" cy="10" r="6" fill="#fff"/><circle cx="140" cy="10" r="3.5" fill="var(--coral)"/>
    </svg>
  </div>
  <nav class="abs navbar" aria-label="Main">
    <svg width="16" height="16" viewBox="0 0 16 16" aria-label="Home"><path d="M2 8 8 2l6 6v6H2z" fill="var(--navy)"/></svg>
    <svg width="16" height="16" viewBox="0 0 16 16" aria-label="Calendar"><rect x="1.5" y="3" width="13" height="11.5" rx="2" stroke="var(--navy)" stroke-width="2" fill="none"/><path d="M1.5 7h13M5 1v3M11 1v3" stroke="var(--navy)" stroke-width="2"/></svg>
    <svg width="16" height="16" viewBox="0 0 16 16" aria-label="Chat"><path d="M1 2h14v10H7l-4 3v-3H1z" fill="var(--navy)"/></svg>
    <svg width="16" height="16" viewBox="0 0 16 16" aria-label="Video tips"><rect x="0.5" y="3" width="10.5" height="10" rx="2" fill="var(--navy)"/><path d="M11 7l4.5-2.5v7L11 9z" fill="var(--navy)"/></svg>
    <svg width="16" height="16" viewBox="0 0 16 16" aria-label="Notes"><rect x="2.5" y="1" width="11" height="14" rx="2" stroke="var(--navy)" stroke-width="2" fill="none"/><path d="M5.5 5.5h5M5.5 8.5h5M5.5 11.5h3" stroke="var(--navy)" stroke-width="1.6"/></svg>
  </nav>
</section>

<section class="screen screen--progress" aria-label="Progress screen">
  <div class="abs hero"></div>
  <div class="topbar">
    <svg width="12" height="12" viewBox="0 0 12 12"><path d="M8 2 4 6l4 4" stroke="#fff" stroke-width="2" fill="none"/></svg>
    <svg width="14" height="12" viewBox="0 0 14 12"><path d="M1 2h12M1 6h12M1 10h12" stroke="#fff" stroke-width="2"/></svg>
  </div>
  <h2 class="abs center title">Current Progress</h2>
  <svg class="abs" style="left:20px;top:162px" width="264" height="20" viewBox="0 0 264 20" aria-hidden="true">
    <path d="M12 2 4 10l8 8" stroke="#fff" stroke-width="2.5" fill="none"/>
    <path d="M252 2l8 8-8 8" stroke="#fff" stroke-width="2.5" fill="none"/>
  </svg>
  <svg class="abs ring" viewBox="0 0 136 136" aria-hidden="true">
    <circle cx="68" cy="68" r="66" fill="var(--sky)"/>
    <circle cx="68" cy="68" r="52" fill="#fff"/>
    <circle cx="68" cy="68" r="46" fill="none" stroke="var(--ice)" stroke-width="6"/>
    <circle cx="68" cy="68" r="46" fill="none" stroke="var(--coral)" stroke-width="6" stroke-dasharray="217 289" transform="rotate(-90 68 68)"/>
  </svg>
  <p class="abs center ring-label">75%</p>
  <p class="abs center ring-sub">Swing goal</p>
  <a class="pill pill--tools">Coach Tools</a>
  <div class="abs tiles">
    <div class="tile"><span><svg width="22" height="22" viewBox="0 0 22 22"><rect x="2" y="4" width="18" height="16" rx="3" stroke="var(--navy)" stroke-width="2" fill="none"/><path d="M2 9h18M7 1v5M15 1v5" stroke="var(--navy)" stroke-width="2"/></svg></span>Calendar</div>
    <div class="tile tile--active"><span><svg width="24" height="18" viewBox="0 0 24 18"><rect x="1" y="2" width="15" height="14" rx="3" fill="#fff"/><path d="M16 7l7-4v12l-7-4z" fill="#fff"/></svg></span>Video tips</div>
    <div class="tile"><span><svg width="22" height="20" viewBox="0 0 22 20"><path d="M2 2h18v12H9l-5 4v-4H2z" stroke="var(--navy)" stroke-width="2" fill="none" stroke-linejoin="round"/></svg></span>Chat</div>
  </div>
  <div class="abs chart" aria-label="Practice sessions per day">
    <div class="bars">
      <div class="bar" style="height:22px"></div>
      <div class="bar" style="height:22px"></div>
      <div class="bar" style="height:22px"></div>
      <div class="bar" style="height:22px"></div>
      <div class="bar bar--hot" style="height:40px"></div>
      <div class="bar" style="height:22px"></div>
      <div class="bar" style="height:22px"></div>
    </div>
    <div class="days"><span>Mon</span><span>Tue</span><span>Wed</span><span>Thu</span><span>Fri</span><span>Sat</span><span>Sun</span></div>
  </div>
  <a class="abs fab" aria-label="Add note">+</a>
</section>

</body>
</html>
```